Brim-Vane PowerPoint Layout Design - Updated

We're now looking for a PowerPoint Layout design for Brim-Vane. Brim-Vane is an innovative, forward thinking insurance technology designed to help Commercially Focused Insurance Brokers and Agents track their organization's strategic performance and all of the individual opportunities that they come in contact with throughout a calendar year. Users gain powerful insights for improvement, efficiencies, and effectiveness that can be shared with their insurance carrier trading partners which, in turn, benefits their clients and the insurance professionals within these same organizations.

```html
<!DOCTYPE html>
<html lang="en">
<head>
<meta charset="utf-8">
<title>Brim-Vane – Presentation Layout Overview</title>
<link href="https://fonts.googleapis.com/css2?family=Exo+2:wght@600;700&family=Montserrat:wght@400;500;600;700&display=swap" rel="stylesheet">
<style>
:root{
  --green:#5e9a45;
  --green-dark:#4d8638;
  --gold:#dfbf55;
  --gold-soft:#efe0a6;
  --ink:#222;
  --grey:#777;
  --paper:#fff;
}
*{margin:0;padding:0;box-sizing:border-box}
html,body{width:1200px;height:757px;overflow:hidden;background:#fff}
.board{position:relative;width:1200px;height:757px}
.slide{position:absolute;width:199px;height:112px;background:var(--paper);overflow:hidden;box-shadow:0 1px 3px rgba(0,0,0,.28);font-family:Montserrat,sans-serif}
.bg{position:absolute;left:0;top:0;width:199px;height:112px}
.a{position:absolute}
.logo{position:absolute;font:600 7px/1 Montserrat,sans-serif;color:var(--green)}
.ttl{position:absolute;left:0;right:0;text-align:center;font:700 4.6px/1 'Exo 2',sans-serif;color:var(--ink)}
.ttl::before{content:"";display:inline-block;width:3px;height:3px;background:var(--green);margin-right:1.5px}
.p{font-family:Montserrat,sans-serif;font-size:1.8px;line-height:1.4;color:var(--grey)}
.h{font-family:Montserrat,sans-serif;font-weight:700;color:var(--ink);font-size:2px;line-height:1.3}
.c{text-align:center}
.r{text-align:right}
.w{color:#fff}
.foot{position:absolute;left:0;right:0;bottom:0;height:10px}
.pg{position:absolute;left:2px;bottom:1px;width:7px;height:8px;background:var(--green)}
.flogo{position:absolute;left:12px;bottom:2px;font:600 5.5px/1 Montserrat,sans-serif;color:var(--green)}
.dots{position:absolute;left:46px;bottom:2.6px;display:flex;gap:1px}
.dots i{display:block;width:3px;height:3px;border-radius:50%;background:#8a8a8a}
.web{position:absolute;right:4px;bottom:2.6px;font:400 1.8px/3px Montserrat,sans-serif;color:#444;display:flex;align-items:center;gap:1px}
.web i{display:block;width:3px;height:3px;border-radius:50%;background:var(--green)}
.foot.light .flogo,.foot.light .web{color:#fff}
.foot.light .dots i{background:#fff}
.foot.light .pg{background:var(--gold)}
.box{position:absolute;display:flex;align-items:center;justify-content:center;color:#fff;font:600 5px/1 Montserrat,sans-serif}
.grid3{position:absolute;display:grid;grid-template-columns:repeat(3,1fr);gap:9px 8px}
.num{font:500 6px/1 Montserrat,sans-serif;color:var(--gold);float:left;margin-right:1px}
</style>
</head>
<body>
<div class="board">

<!-- Row 1 -->
<section class="slide" style="left:39px;top:48px">
  <svg class="bg" viewBox="0 0 199 112"><polygon points="0,0 4,0 27,112 0,112" fill="var(--green)"/><polygon points="88,0 199,0 199,112" fill="var(--gold)"/></svg>
  <div class="logo" style="left:16px;top:9px">Brim-Vane</div>
  <div class="a" style="left:40px;top:43px;font:500 7px/1 Montserrat,sans-serif;color:var(--ink)">WELCOME TO</div>
  <div class="a" style="left:39px;top:51px;font:500 14px/1 Montserrat,sans-serif;color:var(--green)">Brim-Vane</div>
  <div class="a" style="left:40px;top:71px;width:90px;font:400 2.4px/1.5 Montserrat,sans-serif;color:var(--ink)">LOREM IPSUM IS SIMPLY DUMMY TEXT OF THE PRINTING AND TYPESETTING INDUSTRY.</div>
</section>

<section class="slide" style="left:268px;top:48px">
  <div class="logo" style="left:10px;top:4px;font-size:5.5px">Brim-Vane</div>
  <div class="a" style="left:66px;top:5px;font:700 4.5px/1 'Exo 2',sans-serif;color:var(--ink)"><span style="display:inline-block;width:3px;height:3px;background:var(--green);margin-right:1.5px"></span>Insurance Technology</div>
  <div class="logo" style="left:160px;top:4px;font-size:5.5px">Brim-Vane</div>
  <div class="a" role="img" aria-label="Photo of a hand holding a smartphone with app icons" style="left:12px;top:14px;width:88px;height:44px;background:linear-gradient(135deg,#7a5a3a,#c7a277 55%,#e3c78f)"></div>
  <div class="a" role="img" aria-label="Photo of a digital handshake over a glowing network" style="left:104px;top:14px;width:88px;height:44px;background:linear-gradient(135deg,#0c1a2e,#2b4d74 50%,#b06a2c)"></div>
  <div class="a" style="left:15px;top:50px;width:80px;height:47px;background:var(--gold);padding:4px 5px">
    <div class="h" style="font-size:2.1px">SED UT PERSPICIATIS UNDE OMNIS ISTE NATUS ERROR SIT VOLUPTATEM</div>
    <div class="p" style="color:#3a3320;margin-top:2px;font-size:1.7px">Sed ut perspiciatis unde omnis iste natus error sit voluptatem accusantium doloremque laudantium, totam rem aperiam, eaque ipsa quae ab illo inventore veritatis et quasi architecto beatae vitae dicta sunt explicabo. Nemo enim ipsam voluptatem quia voluptas sit aspernatur aut odit aut fugit, sed quia consequuntur magni dolores eos qui ratione voluptatem sequi nesciunt. Neque porro quisquam est, qui dolorem ipsum quia dolor sit amet.</div>
  </div>
  <div class="a" style="left:109px;top:50px;width:80px;height:47px;background:var(--gold);padding:4px 5px">
    <div class="h" style="font-size:2.1px">SED UT PERSPICIATIS UNDE OMNIS ISTE NATUS ERROR SIT VOLUPTATEM</div>
    <div class="p" style="color:#3a3320;margin-top:2px;font-size:1.7px">Sed ut perspiciatis unde omnis iste natus error sit voluptatem accusantium doloremque laudantium, totam rem aperiam, eaque ipsa quae ab illo inventore veritatis et quasi architecto beatae vitae dicta sunt explicabo. Nemo enim ipsam voluptatem quia voluptas sit aspernatur aut odit aut fugit, sed quia consequuntur magni dolores eos qui ratione voluptatem sequi nesciunt. Neque porro quisquam est, qui dolorem ipsum quia dolor sit amet.</div>
  </div>
  <div class="foot"><span class="pg"></span><span class="flogo">Brim-Vane</span><span class="dots"><i></i><i></i><i></i></span><span class="web"><i></i>www.brim-vane.com</span></div>
</section>

<section class="slide" style="left:496px;top:48px">
  <div class="ttl" style="top:11px">Our Services</div>
  <div class="a p c" style="left:22px;right:22px;top:19px">Omnis iste natus error sit voluptatem accusantium doloremque laudantium, totam rem aperiam, eaque ipsa quae ab illo inventore veritatis et quasi architecto beatae vitae dicta sunt explicabo. Nemo enim ipsam voluptatem quia voluptas sit aspernatur aut odit.</div>
  <div class="grid3" style="left:17px;top:40px;width:165px">
    <div><span class="num">1.</span><div class="h" style="font-size:1.7px">VOLUPTATEM ACCUSANTIUM DOLOREMQUE LAUD.</div><div class="p" style="clear:both;font-size:1.5px;margin-top:2px">Wersplciatis unde omnis iste natus error sit voluptatem accusantium doloremque laudantium, totam rem aperiam.</div></div>
    <div><span class="num">2.</span><div class="h" style="font-size:1.7px">VOLUPTATEM ACCUSANTIUM DOLOREMQUE LAUD.</div><div class="p" style="clear:both;font-size:1.5px;margin-top:2px">Wersplciatis unde omnis iste natus error sit voluptatem accusantium doloremque laudantium, totam rem aperiam.</div></div>
    <div><span class="num">3.</span><div class="h" style="font-size:1.7px">VOLUPTATEM ACCUSANTIUM DOLOREMQUE LAUD.</div><div class="p" style="clear:both;font-size:1.5px;margin-top:2px">Wersplciatis unde omnis iste natus error sit voluptatem accusantium doloremque laudantium, totam rem aperiam.</div></div>
    <div><span class="num">4.</span><div class="h" style="font-size:1.7px">VOLUPTATEM ACCUSANTIUM DOLOREMQUE LAUD.</div><div class="p" style="clear:both;font-size:1.5px;margin-top:2px">Wersplciatis unde omnis iste natus error sit voluptatem accusantium doloremque laudantium, totam rem aperiam.</div></div>
    <div><span class="num">5.</span><div class="h" style="font-size:1.7px">VOLUPTATEM ACCUSANTIUM DOLOREMQUE LAUD.</div><div class="p" style="clear:both;font-size:1.5px;margin-top:2px">Wersplciatis unde omnis iste natus error sit voluptatem accusantium doloremque laudantium, totam rem aperiam.</div></div>
    <div><span class="num">6.</span><div class="h" style="font-size:1.7px">VOLUPTATEM ACCUSANTIUM DOLOREMQUE LAUD.</div><div class="p" style="clear:both;font-size:1.5px;margin-top:2px">Wersplciatis unde omnis iste natus error sit voluptatem accusantium doloremque laudantium, totam rem aperiam.</div></div>
  </div>
  <div class="foot"><span class="pg"></span><span class="flogo">Brim-Vane</span><span class="dots"><i></i><i></i><i></i></span><span class="web"><i></i>www.brim-vane.com</span></div>
</section>

<section class="slide" style="left:725px;top:48px">
  <div class="ttl" style="top:11px">A Sip of Profitability</div>
  <div class="a p c" style="left:22px;right:22px;top:19px;font-size:1.7px">Omnis iste natus error sit voluptatem accusantium doloremque laudantium, totam rem aperiam, eaque ipsa quae ab illo inventore veritatis et quasi architecto beatae vitae dicta sunt explicabo.</div>
  <svg class="bg" viewBox="0 0 199 112">
    <g font-family="Montserrat,sans-serif" font-weight="700" font-size="5.5" fill="#fff" text-anchor="middle">
      <circle cx="38" cy="50" r="15" fill="var(--gold-soft)"/><circle cx="38" cy="50" r="11.5" fill="var(--gold)" stroke="#fff" stroke-width=".8"/><text x="38" y="52">100%</text>
      <circle cx="80" cy="50" r="15" fill="var(--gold-soft)"/><circle cx="80" cy="50" r="11.5" fill="var(--green)" stroke="#fff" stroke-width=".8"/><text x="80" y="52">70%</text>
      <circle cx="122" cy="50" r="15" fill="var(--gold-soft)"/><circle cx="122" cy="50" r="11.5" fill="var(--gold)" stroke="#fff" stroke-width=".8"/><text x="122" y="52">50%</text>
      <circle cx="165" cy="50" r="15" fill="var(--gold-soft)"/><circle cx="165" cy="50" r="11.5" fill="var(--green)" stroke="#fff" stroke-width=".8"/><text x="165" y="52">40%</text>
    </g>
    <g font-family="Montserrat,sans-serif" font-weight="600" font-size="1.9" fill="#fff" text-anchor="middle">
      <polygon points="34,69 38,65.5 42,69" fill="var(--green)"/><rect x="19.5" y="69" width="37" height="10" fill="var(--green)"/><text x="38" y="74.6">Consectetur Adipiscin</text>
      <polygon points="76,69 80,65.5 84,69" fill="var(--gold)"/><rect x="61.5" y="69" width="37" height="10" fill="var(--gold)"/><text x="80" y="74.6">Consectetur Adipiscin</text>
      <polygon points="118,69 122,65.5 126,69" fill="var(--green)"/><rect x="103.5" y="69" width="37" height="10" fill="var(--green)"/><text x="122" y="74.6">Consectetur Adipiscin</text>
      <polygon points="161,69 165,65.5 169,69" fill="var(--gold)"/><rect x="146.5" y="69" width="37" height="10" fill="var(--gold)"/><text x="165" y="74.6">Consectetur Adipiscin</text>
    </g>
  </svg>
  <div class="foot"><span class="pg"></span><span class="flogo">Brim-Vane</span><span class="dots"><i></i><i></i><i></i></span><span class="web"><i></i>www.brim-vane.com</span></div>
</section>

<section class="slide" style="left:953px;top:48px">
  <div class="ttl" style="top:6px">Benefits</div>
  <svg class="bg" viewBox="0 0 199 112">
    <circle cx="100" cy="47" r="26" fill="none" stroke="var(--green)" stroke-width=".35"/>
    <circle cx="100" cy="47" r="20" fill="var(--green)"/>
    <circle cx="100" cy="47" r="21.5" fill="none" stroke="var(--green)" stroke-width=".8"/>
    <g fill="#fff" stroke="var(--green)" stroke-width=".35">
      <circle cx="76" cy="36" r="1.3"/><circle cx="124" cy="36" r="1.3"/><circle cx="74.5" cy="55" r="1.3"/><circle cx="125.5" cy="55" r="1.3"/><circle cx="100" cy="73" r="1.3"/>
    </g>
  </svg>
  <div class="a c" style="left:16px;top:19px;width:58px"><div class="h" style="font-size:1.6px">Faerspiciatis unde omnis iste natus error sit voluptatem</div><div class="p" style="font-size:1.4px">Wersplciatis unde omnis iste natus error sit voluptate massea accusantium dolorem quelaudium, totam rem aperiam.</div></div>
  <div class="a c" style="left:126px;top:19px;width:58px"><div class="h" style="font-size:1.6px">Faerspiciatis unde omnis iste natus error sit voluptatem</div><div class="p" style="font-size:1.4px">Wersplciatis unde omnis iste natus error sit voluptate massea accusantium dolorem quelaudium, totam rem aperiam.</div></div>
  <div class="a c" style="left:13px;top:53px;width:58px"><div class="h" style="font-size:1.6px">Faerspiciatis unde omnis iste natus error sit voluptatem</div><div class="p" style="font-size:1.4px">Wersplciatis unde omnis iste natus error sit voluptate massea accusantium dolorem quelaudium, totam rem aperiam.</div></div>
  <div class="a c" style="left:129px;top:53px;width:58px"><div class="h" style="font-size:1.6px">Faerspiciatis unde omnis iste natus error sit voluptatem</div><div class="p" style="font-size:1.4px">Wersplciatis unde omnis iste natus error sit voluptate massea accusantium dolorem quelaudium, totam rem aperiam.</div></div>
  <div class="a c" style="left:55px;top:82px;width:90px"><div class="h" style="font-size:1.6px">Faerspiciatis unde omnis iste natus error sit voluptatem</div><div class="p" style="font-size:1.4px">Wersplciatis unde omnis iste natus error sit voluptate massea accusantium dolorem quelaudium, totam rem aperiam.</div></div>
  <div class="foot"><span class="pg"></span><span class="flogo">Brim-Vane</span><span class="dots"><i></i><i></i><i></i></span><span class="web"><i></i>www.brim-vane.com</span></div>
</section>

<!-- Row 2 -->
<section class="slide" style="left:39px;top:187px">
  <svg class="bg" viewBox="0 0 199 112"><polygon points="0,0 4,0 27,112 0,112" fill="var(--green)"/><polygon points="88,0 199,0 199,112" fill="var(--gold)"/></svg>
  <div class="logo" style="left:16px;top:9px">Brim-Vane</div>
  <div class="a" style="left:24px;top:33px;font:700 8px/1 'Exo 2',sans-serif;color:var(--ink)"><span style="display:inline-block;width:5px;height:5px;background:var(--green);margin-right:2px"></span>Agenda</div>
  <div class="a" style="left:24px;top:48px;width:102px;font:400 4px/10px Montserrat,sans-serif;color:#999">
    <div style="display:flex;justify-content:space-between"><span>Sed ut perspiciatis unde omnis iste natus</span><span>03</span></div>
    <div style="display:flex;justify-content:space-between"><span>Error sit voluptatem accusantium</span><span>04</span></div>
    <div style="display:flex;justify-content:space-between"><span>Doloremque laudantium</span><span>15</span></div>
    <div style="display:flex;justify-content:space-between"><span>Ut enim ad minima veniam, quis nostrum</span><span>19</span></div>
    <div style="display:flex;justify-content:space-between"><span>Exercitationem ullam corporis</span><span>31</span></div>
  </div>
</section>

<section class="slide" style="left:268px;top:187px">
  <svg class="bg" viewBox="0 0 199 112"><polygon points="176,0 199,0 199,20" fill="var(--gold)"/></svg>
  <div class="a" style="left:9px;top:8px;font:700 8px/1 'Exo 2',sans-serif;color:var(--ink)"><span style="display:inline-block;width:5px;height:5px;background:var(--green);margin-right:2px"></span>How It Works</div>
  <div class="box" style="left:9px;top:27px;width:17px;height:13px;background:var(--gold)">01</div>
  <div class="box" style="left:101px;top:27px;width:17px;height:13px;background:var(--green)">02</div>
  <div class="box" style="left:9px;top:54px;width:17px;height:13px;background:var(--green)">03</div>
  <div class="box" style="left:101px;top:54px;width:17px;height:13px;background:var(--gold)">04</div>
  <div class="box" style="left:9px;top:80px;width:17px;height:13px;background:var(--gold)">05</div>
  <div class="box" style="left:101px;top:80px;width:17px;height:13px;background:var(--green)">06</div>
  <div class="a p" style="left:31px;top:26px;width:56px;font-size:2.6px;color:#aaa">Sed ut perspiciatis unde omnis iste natus error sit voluptatem accusantium doloremque</div>
  <div class="a p" style="left:123px;top:26px;width:56px;font-size:2.6px;color:#aaa">Nemo enim ipsam voluptatem quia voluptas sit aspernatur aut odit aut fugit, sed quia</div>
  <div class="a p" style="left:31px;top:53px;width:56px;font-size:2.6px;color:#aaa">Sed ut perspiciatis unde omnis iste natus error sit voluptatem accusantium doloremque</div>
  <div class="a p" style="left:123px;top:53px;width:56px;font-size:2.6px;color:#aaa">Nemo enim ipsam voluptatem quia voluptas sit aspernatur aut odit aut fugit, sed quia</div>
  <div class="a p" style="left:31px;top:79px;width:56px;font-size:2.6px;color:#aaa">Sed ut perspiciatis unde omnis iste natus error sit voluptatem accusantium doloremque</div>
  <div class="a p" style="left:123px;top:79px;width:56px;font-size:2.6px;color:#aaa">Nemo enim ipsam voluptatem quia voluptas sit aspernatur aut odit aut fugit, sed quia</div>
  <div class="foot"><span class="pg"></span><span class="flogo">Brim-Vane</span><span class="dots"><i></i><i></i><i></i></span><span class="web"><i></i>www.brim-vane.com</span></div>
</section>

<section class="slide" style="left:496px;top:187px">
  <div class="a" role="img" aria-label="Faded photo of a city skyline above an open plaza" style="inset:0;background:linear-gradient(180deg,#f4f4f4 0%,#d9d9d9 35%,#ececec 60%,#fafafa 100%)"></div>
  <div class="a c" style="left:0;right:0;top:47px;font:600 17px/1 Montserrat,sans-serif;color:var(--green)">Brim-Vane</div>
</section>

<section class="slide" style="left:725px;top:187px">
  <div class="a" style="left:8px;top:8px;font:700 4.6px/1 'Exo 2',sans-serif;color:var(--ink)"><span style="display:inline-block;width:3px;height:3px;background:var(--green);margin-right:1.5px"></span>About Us</div>
  <div class="a p" style="left:8px;top:18px;width:90px;text-align:justify;color:#444">Lorem ipsum dolor sit amet, consectetur adipiscing elit, sed do eiusmod tempor incididunt ut labore et dolore magna aliqua. Ut enim ad minim veniam, quis nostrud exercitation ullamco laboris nisi ut aliquip ex ea commodo consequat. Duis aute irure dolor in reprehenderit in voluptate velit esse cillum dolore eu fugiat nulla pariatur. Excepteur sint occaecat cupidatat non proident, sunt in culpa qui officia deserunt mollit anim id est laborum.<br><br>Lorem ipsum dolor sit amet, consectetur adipiscing elit, sed do eiusmod tempor incididunt ut labore et dolore magna aliqua. Ut enim ad minim veniam, quis nostrud exercitation ullamco laboris nisi ut aliquip ex ea commodo consequat. Duis aute irure dolor in reprehenderit in voluptate velit esse cillum dolore eu fugiat nulla pariatur. Excepteur sint occaecat cupidatat non proident, sunt in culpa qui officia deserunt mollit anim id est laborum.</div>
  <svg class="bg" viewBox="0 0 199 112">
    <defs><linearGradient id="aboutPhoto" x1="0" y1="0" x2="1" y2="1"><stop offset="0" stop-color="#4a4a4a"/><stop offset=".5" stop-color="#a89a86"/><stop offset="1" stop-color="#d6cfc3"/></linearGradient></defs>
    <circle cx="162" cy="48" r="52" fill="url(#aboutPhoto)" role="img" aria-label="Photo of a team reviewing charts at a desk"/>
    <circle cx="162" cy="48" r="20" fill="none" stroke="#ddd" stroke-width="4" stroke-dasharray="90 40" opacity=".8"/>
  </svg>
  <div class="foot"><span class="pg"></span><span class="flogo">Brim-Vane</span><span class="dots"><i></i><i></i><i></i></span><span class="web"><i></i>www.brim-vane.com</span></div>
</section>

<section class="slide" style="left:953px;top:187px">
  <div class="a" role="img" aria-label="Photo of a hand working on documents under a green tint" style="inset:0;background:linear-gradient(120deg,#8fae3e 0%,#6b9a3f 45%,#4f8a3a 100%)"></div>
  <div class="a c w" style="left:0;right:0;top:42px;font:600 7px/1 'Exo 2',sans-serif">EXCEPTEUR SINT OCCAECAT CUPIDATAT</div>
  <div class="a c" style="left:10px;right:10px;top:52px;font:400 4px/1.3 Montserrat,sans-serif;color:#eef3e4">Sed ut perspiciatis unde omnis iste natus error sit voluptatem accusantium doloremque laudantium, totam rem aperiam, eaque ipsa quae ab illo inventore veritatis et quasi.</div>
  <div class="foot light"><span class="pg"></span><span class="flogo">Brim-Vane</span><span class="dots"><i></i><i></i><i></i></span><span class="web"><i></i>www.brim-vane.com</span></div>
</section>

<!-- Row 3 -->
<section class="slide" style="left:39px;top:326px">
  <div class="ttl" style="top:9px">Solution</div>
  <svg class="bg" viewBox="0 0 199 112">
    <g fill="var(--green)">
      <polygon points="28,46.5 32,43 97,43 97,50 32,50"/>
      <polygon points="103,43 168,43 172,46.5 168,50 103,50"/>
      <polygon points="28,73.5 32,70 97,70 97,77 32,77"/>
      <polygon points="103,70 168,70 172,73.5 168,77 103,77"/>
    </g>
    <polygon points="100,44 113,58 100,72 87,58" fill="#c9b9a6" role="img" aria-label="Photo of two colleagues working together"/>
    <g fill="var(--gold)">
      <polygon points="88,28 92.5,30.5 92.5,35.5 88,38 83.5,35.5 83.5,30.5"/>
      <polygon points="112,28 116.5,30.5 116.5,35.5 112,38 107.5,35.5 107.5,30.5"/>
      <polygon points="88,78 92.5,80.5 92.5,85.5 88,88 83.5,85.5 83.5,80.5"/>
      <polygon points="112,78 116.5,80.5 116.5,85.5 112,88 107.5,85.5 107.5,80.5"/>
    </g>
    <g fill="#fff"><circle cx="88" cy="33" r="1.5"/><circle cx="112" cy="33" r="1.5"/><circle cx="88" cy="83" r="1.5"/><circle cx="112" cy="83" r="1.5"/></g>
    <g font-family="Montserrat,sans-serif" font-weight="600" font-size="2.2" fill="#fff" text-anchor="middle">
      <text x="62" y="47.4">Lorem ipsum dolor sit amet</text><text x="138" y="47.4">Lorem ipsum dolor sit amet</text>
      <text x="62" y="74.4">Lorem ipsum dolor sit amet</text><text x="138" y="74.4">Lorem ipsum dolor sit amet</text>
    </g>
  </svg>
  <div class="a c h" style="left:20px;top:21px;width:60px;font-size:1.6px;font-weight:600">Lorem ipsum dolor sit amet, consectetur adipiscing elit, sed do eiusmod tempor incididunt ut labore et dolore magna aliqua. Ut enim ad minim, quis nostrud exercitation ullamco</div>
  <div class="a c h" style="left:120px;top:21px;width:60px;font-size:1.6px;font-weight:600">Lorem ipsum dolor sit amet, consectetur adipiscing elit, sed do eiusmod tempor incididunt ut labore et dolore magna aliqua. Ut enim ad minim, quis nostrud exercitation ullamco</div>
  <div class="a c h" style="left:20px;top:79px;width:60px;font-size:1.6px;font-weight:600">Lorem ipsum dolor sit amet, consectetur adipiscing elit, sed do eiusmod tempor incididunt ut labore et dolore magna aliqua. Ut enim ad minim, quis nostrud exercitation ullamco</div>
  <div class="a c h" style="left:120px;top:79px;width:60px;font-size:1.6px;font-weight:600">Lorem ipsum dolor sit amet, consectetur adipiscing elit, sed do eiusmod tempor incididunt ut labore et dolore magna aliqua. Ut enim ad minim, quis nostrud exercitation ullamco</div>
  <div class="foot"><span class="pg"></span><span class="flogo">Brim-Vane</span><span class="dots"><i></i><i></i><i></i></span><span class="web"><i></i>www.brim-vane.com</span></div>
</section>

<section class="slide" style="left:268px;top:326px">
  <div class="ttl" style="top:18px">Infographics</div>
  <svg class="bg" viewBox="0 0 199 112">
    <g fill="none" stroke="var(--gold)" stroke-width=".7"><circle cx="91" cy="41" r="10.5"/><circle cx="117" cy="41" r="10.5"/><circle cx="91" cy="71" r="10.5"/><circle cx="117" cy="71" r="10.5"/></g>
    <g fill="var(--gold)"><circle cx="91" cy="41" r="8.5"/><circle cx="117" cy="41" r="8.5"/><circle cx="91" cy="71" r="8.5"/><circle cx="117" cy="71" r="8.5"/></g>
    <g fill="none" stroke="#fff" stroke-width=".7"><circle cx="91" cy="41" r="3"/><circle cx="117" cy="41" r="3"/><rect x="88" y="68.5" width="6" height="5"/><circle cx="117" cy="71" r="3"/></g>
  </svg>
  <div class="a r" style="left:22px;top:34px;width:57px"><div class="h" style="font-size:2.8px;font-weight:600">Duis aute irure dolor</div><div class="p" style="font-size:1.7px;color:#555">Lorem ipsum dolor sit amet, consectetur adipiscing elit, sed do eiusmod tempor incididunt ut labore et dolore magna aliqua.</div></div>
  <div class="a" style="left:130px;top:34px;width:57px"><div class="h" style="font-size:2.8px;font-weight:600">Duis aute irure dolor</div><div class="p" style="font-size:1.7px;color:#555">Lorem ipsum dolor sit amet, consectetur adipiscing elit, sed do eiusmod tempor incididunt ut labore et dolore magna aliqua.</div></div>
  <div class="a r" style="left:22px;top:64px;width:57px"><div class="h" style="font-size:2.8px;font-weight:600">Duis aute irure dolor</div><div class="p" style="font-size:1.7px;color:#555">Lorem ipsum dolor sit amet, consectetur adipiscing elit, sed do eiusmod tempor incididunt ut labore et dolore magna aliqua.</div></div>
  <div class="a" style="left:130px;top:64px;width:57px"><div class="h" style="font-size:2.8px;font-weight:600">Duis aute irure dolor</div><div class="p" style="font-size:1.7px;color:#555">Lorem ipsum dolor sit amet, consectetur adipiscing elit, sed do eiusmod tempor incididunt ut labore et dolore magna aliqua.</div></div>
  <div class="foot"><span class="pg"></span><span class="flogo">Brim-Vane</span><span class="dots"><i></i><i></i><i></i></span><span class="web"><i></i>www.brim-vane.com</span></div>
</section>

<section class="slide" style="left:496px;top:326px">
  <div class="a" role="img" aria-label="Faded photo of a city skyline" style="inset:0;background:linear-gradient(180deg,#f6f6f6 0%,#dcdcdc 40%,#eeeeee 70%,#fafafa 100%)"></div>
  <div class="a c" style="left:0;right:0;top:28px;font:500 11px/1 Montserrat,sans-serif;color:var(--ink)">Thank You</div>
  <svg class="bg" viewBox="0 0 199 112">
    <g fill="var(--gold)"><circle cx="57" cy="55" r="4"/><circle cx="101" cy="55" r="4"/><circle cx="144" cy="55" r="4"/></g>
    <path d="M57 53a1.4 1.4 0 1 1 0 .01M57 57.3l-1.6-2.6a1.9 1.9 0 1 1 3.2 0z" fill="#fff"/>
    <path d="M99.6 53.4c.4 1.6 1.4 2.6 3 3l.6-.8-1-.6-.5.4c-.6-.3-1-.7-1.3-1.3l.4-.5-.6-1z" fill="#fff"/>
    <rect x="142.2" y="53.8" width="3.6" height="2.6" fill="#fff"/><path d="M142.2 53.8l1.8 1.4 1.8-1.4" stroke="var(--gold)" stroke-width=".3" fill="none"/>
    <g stroke="#bbb" stroke-width=".25"><line x1="80" y1="60" x2="80" y2="76"/><line x1="122" y1="60" x2="122" y2="76"/></g>
  </svg>
  <div class="a c h" style="left:37px;top:63px;width:40px;font-size:1.7px;font-weight:600">ADDRESS:</div>
  <div class="a c p" style="left:37px;top:67px;width:40px;font-size:1.6px">123 Lorem ipsum dolor sit amet, consectetur</div>
  <div class="a c h" style="left:81px;top:63px;width:40px;font-size:1.7px;font-weight:600">PHONE:</div>
  <div class="a c p" style="left:81px;top:67px;width:40px;font-size:1.6px">+1 888 888 8888</div>
  <div class="a c h" style="left:124px;top:63px;width:40px;font-size:1.7px;font-weight:600">EMAIL ADDRESS:</div>
  <div class="a c p" style="left:124px;top:67px;width:40px;font-size:1.6px">info@companyname.com</div>
  <div class="foot"><span class="pg"></span><span class="flogo">Brim-Vane</span><span class="dots"><i></i><i></i><i></i></span><span class="web"><i></i>www.brim-vane.com</span></div>
</section>

<section class="slide" style="left:725px;top:326px">
  <div class="ttl" style="top:9px">Why Choose Us</div>
  <svg class="bg" viewBox="0 0 199 112">
    <path d="M158 18a40 40 0 1 0 0 80" fill="none" stroke="var(--gold)" stroke-width=".4"/>
    <circle cx="157" cy="58" r="35" fill="var(--green)"/>
    <circle cx="157" cy="58" r="31" fill="var(--gold)"/>
    <g fill="var(--green)" stroke="var(--gold)" stroke-width=".8"><circle cx="108" cy="31" r="4"/><circle cx="100" cy="48" r="4"/><circle cx="100" cy="66" r="4"/><circle cx="108" cy="84" r="4"/></g>
    <g fill="#fff"><circle cx="108" cy="31" r="1.3"/><circle cx="100" cy="48" r="1.3"/><circle cx="100" cy="66" r="1.3"/><circle cx="108" cy="84" r="1.3"/></g>
  </svg>
  <div class="a c" style="left:136px;top:40px;width:42px"><div class="h w" style="font-size:2.4px;font-weight:600">Lorem ipsum dolor sit amet consectetur adi</div><div class="p w" style="font-size:1.5px;margin-top:2px">Lorem ipsum dolor sit amet, consectetur adipiscing elit, sed do eiusmod tempor incididunt ut labore et dolore magna aliqua. Ut enim ad minim veniam, quis nostrud exercitation ullamco laboris nisi ut aliquip.</div></div>
  <div class="a r" style="left:22px;top:27px;width:80px"><div class="h" style="font-size:1.6px">Lorem ipsum dolor sit ameted consectetur adied</div><div class="p" style="font-size:1.4px">Lorem ipsum dolor sit amet, consectetur adipiscing elit, sed do eiusmod tempor incididunt ut labore et dolore magna aliqua.</div></div>
  <div class="a r" style="left:14px;top:44px;width:80px"><div class="h" style="font-size:1.6px">Lorem ipsum dolor sit ameted consectetur adied</div><div class="p" style="font-size:1.4px">Lorem ipsum dolor sit amet, consectetur adipiscing elit, sed do eiusmod tempor incididunt ut labore et dolore magna aliqua.</div></div>
  <div class="a r" style="left:14px;top:62px;width:80px"><div class="h" style="font-size:1.6px">Lorem ipsum dolor sit ameted consectetur adied</div><div class="p" style="font-size:1.4px">Lorem ipsum dolor sit amet, consectetur adipiscing elit, sed do eiusmod tempor incididunt ut labore et dolore magna aliqua.</div></div>
  <div class="a r" style="left:22px;top:80px;width:80px"><div class="h" style="font-size:1.6px">Lorem ipsum dolor sit ameted consectetur adied</div><div class="p" style="font-size:1.4px">Lorem ipsum dolor sit amet, consectetur adipiscing elit, sed do eiusmod tempor incididunt ut labore et dolore magna aliqua.</div></div>
  <div class="foot"><span class="pg"></span><span class="flogo">Brim-Vane</span><span class="dots"><i></i><i></i><i></i></span><span class="web"><i></i>www.brim-vane.com</span></div>
</section>

<section class="slide" style="left:953px;top:326px">
  <div class="ttl" style="top:9px">Infographics</div>
  <svg class="bg" viewBox="0 0 199 112">
    <polygon points="44.5,24 64.5,59 24.5,59" fill="var(--green)"/>
    <polygon points="23,62 42.5,95 3,95" fill="var(--gold)"/>
    <polygon points="66,62 85.5,95 46.5,95" fill="var(--gold)"/>
    <g fill="var(--green)"><circle cx="103" cy="33" r="6"/><circle cx="103" cy="59" r="6"/><circle cx="103" cy="85" r="6"/></g>
    <g fill="none" stroke="#fff" stroke-width=".5"><circle cx="103" cy="33" r="2.6"/><circle cx="103" cy="58" r="1.6"/><path d="M100 62c0-2 6-2 6 0"/><rect x="100.5" y="82.5" width="5" height="5"/></g>
  </svg>
  <div class="a c w" style="left:28px;top:41px;width:33px"><div style="font:600 2.3px/1.2 Montserrat,sans-serif">Lorem dolor</div><div style="font:400 1.4px/1.4 Montserrat,sans-serif">Sed ut perspiciatis unde omnis iste natus error sit voluptatem accusantium</div></div>
  <div class="a c w" style="left:8px;top:77px;width:30px"><div style="font:600 2.3px/1.2 Montserrat,sans-serif">Lorem dolor</div><div style="font:400 1.4px/1.4 Montserrat,sans-serif">Sed ut perspiciatis unde omnis iste natus error sit voluptatem accusantium</div></div>
  <div class="a c w" style="left:51px;top:77px;width:30px"><div style="font:600 2.3px/1.2 Montserrat,sans-serif">Lorem dolor</div><div style="font:400 1.4px/1.4 Montserrat,sans-serif">Sed ut perspiciatis unde omnis iste natus error sit voluptatem accusantium</div></div>
  <div class="a" style="left:113px;top:26px;width:80px"><div class="h" style="font-size:2.3px;font-weight:600">Lorem ipsum dolor</div><div class="p" style="font-size:1.6px">Sed ut perspiciatis unde omnis iste natus error sit voluptatem accusantium doloremque laudantium, totam rem aperiam, eaque ipsa quae ab illo inventore veritatis et quasi architecto beatae vitae dicta sunt explicabo.</div></div>
  <div class="a" style="left:113px;top:52px;width:80px"><div class="h" style="font-size:2.3px;font-weight:600">Lorem ipsum dolor</div><div class="p" style="font-size:1.6px">Sed ut perspiciatis unde omnis iste natus error sit voluptatem accusantium doloremque laudantium, totam rem aperiam, eaque ipsa quae ab illo inventore veritatis et quasi architecto beatae vitae dicta sunt explicabo.</div></div>
  <div class="a" style="left:113px;top:78px;width:80px"><div class="h" style="font-size:2.3px;font-weight:600">Lorem ipsum dolor</div><div class="p" style="font-size:1.6px">Sed ut perspiciatis unde omnis iste natus error sit voluptatem accusantium doloremque laudantium, totam rem aperiam, eaque ipsa quae ab illo inventore veritatis et quasi architecto beatae vitae dicta sunt explicabo.</div></div>
  <div class="foot"><span class="pg"></span><span class="flogo">Brim-Vane</span><span class="dots"><i></i><i></i><i></i></span><span class="web"><i></i>www.brim-vane.com</span></div>
</section>

<!-- Row 4 -->
<section class="slide" style="left:39px;top:465px">
  <svg class="bg" viewBox="0 0 199 112" role="img" aria-label="Collage of business people photos in slanted panels">
    <defs>
      <linearGradient id="col1" x1="0" y1="0" x2="1" y2="1"><stop offset="0" stop-color="#b9b4ac"/><stop offset="1" stop-color="#7f776c"/></linearGradient>
      <linearGradient id="col2" x1="0" y1="0" x2="1" y2="1"><stop offset="0" stop-color="#d9cbb6"/><stop offset="1" stop-color="#8a6a4c"/></linearGradient>
      <linearGradient id="col3" x1="0" y1="0" x2="1" y2="1"><stop offset="0" stop-color="#6e5443"/><stop offset="1" stop-color="#c9b49a"/></linearGradient>
      <linearGradient id="col4" x1="0" y1="0" x2="1" y2="1"><stop offset="0" stop-color="#d7d4cf"/><stop offset="1" stop-color="#4f4a45"/></linearGradient>
    </defs>
    <polygon points="0,0 30,0 0,45" fill="url(#col1)"/>
    <polygon points="36,0 80,0 46,48 3,48" fill="url(#col2)"/>
    <polygon points="0,52 44,52 22,112 0,112" fill="url(#col3)"/>
    <polygon points="50,52 100,52 74,112 28,112" fill="url(#col4)"/>
  </svg>
  <div class="logo" style="right:6px;top:7px;font-size:5.5px">Brim-Vane</div>
  <div class="a" style="left:126px;top:34px;height:8px;width:1.3px;background:var(--green)"></div>
  <div class="a" style="left:130px;top:35px;font:500 7px/1 Montserrat,sans-serif;color:var(--ink)">TITLE GOES <span style="color:var(--gold)">HERE</span></div>
  <div class="a" style="left:133px;top:49px;font:500 4px/1 Montserrat,sans-serif;color:var(--gold)">Presenter Name</div>
  <svg class="bg" viewBox="0 0 199 112">
    <g fill="var(--gold)">
      <path d="M134 58.4c.4 1.6 1.4 2.6 3 3l.6-.8-1-.6-.5.4c-.6-.3-1-.7-1.3-1.3l.4-.5-.6-1z"/>
      <circle cx="135.5" cy="68" r="1.8" fill="none" stroke="var(--gold)" stroke-width=".4"/>
      <rect x="133.7" y="75.6" width="3.6" height="2.6"/>
      <path d="M135.5 88.5l-1.6-2.6a1.9 1.9 0 1 1 3.2 0z"/>
    </g>
  </svg>
  <div class="a" style="left:141px;top:58px;font:500 2.6px/9px Montserrat,sans-serif;color:var(--ink)">+1 (888) 888 8888<br>www.yourwebsite.com<br>info@brimvane.com<br>Add your Location here</div>
</section>

<section class="slide" style="left:268px;top:465px;background:var(--gold)">
  <div class="foot light"><span class="pg" style="background:var(--green)"></span><span class="flogo">Brim-Vane</span><span class="dots"><i></i><i></i><i></i></span><span class="web"><i style="background:var(--green)"></i>www.brim-vane.com</span></div>
</section>

<section class="slide" style="left:496px;top:465px;background:var(--green)">
  <div class="foot light"><span class="pg"></span><span class="flogo">Brim-Vane</span><span class="dots"><i></i><i></i><i></i></span><span class="web"><i style="background:var(--gold)"></i>www.brim-vane.com</span></div>
</section>

<section class="slide" style="left:725px;top:465px">
  <div class="ttl" style="top:9px">Meet Our Team</div>
  <div class="a p c" style="left:14px;right:14px;top:18px;font-size:1.7px;color:#555">Nemo enim ipsam voluptatem quia voluptas sit aspernatur aut odit aut fugit, sed quia consequuntur magni dolores eos qui ratione voluptatem sequi nesciunt. Neque porro quisquam est, qui dolorem ipsum quia dolor sit amet.</div>
  <svg class="bg" viewBox="0 0 199 112">
    <g fill="var(--green)">
      <polygon points="7,53 66,32 66,95 7,95"/>
      <polygon points="70,53 129,32 129,95 70,95"/>
      <polygon points="133,53 192,32 192,95 133,95"/>
    </g>
    <g fill="#b8ada0" stroke="#fff" stroke-width="1">
      <circle cx="37" cy="41" r="13" role="img" aria-label="Team member portrait photo"/>
      <circle cx="100" cy="41" r="13" role="img" aria-label="Team member portrait photo"/>
      <circle cx="163" cy="41" r="13" role="img" aria-label="Team member portrait photo"/>
    </g>
  </svg>
  <div class="a c w" style="left:9px;top:67px;width:56px"><div style="font:700 3.2px/1 'Exo 2',sans-serif">NAME HEADING</div><div style="font:400 1.5px/1.4 Montserrat,sans-serif;margin-top:2px">Nemo enim ipsam voluptatem quia voluptas sit aspernatur aut odit aut fugit, sed quia consequuntur magni dolores eos qui ratione voluptatem.</div></div>
  <div class="a c w" style="left:72px;top:67px;width:56px"><div style="font:700 3.2px/1 'Exo 2',sans-serif">NAME HEADING</div><div style="font:400 1.5px/1.4 Montserrat,sans-serif;margin-top:2px">Nemo enim ipsam voluptatem quia voluptas sit aspernatur aut odit aut fugit, sed quia consequuntur magni dolores eos qui ratione voluptatem.</div></div>
  <div class="a c w" style="left:135px;top:67px;width:56px"><div style="font:700 3.2px/1 'Exo 2',sans-serif">NAME HEADING</div><div style="font:400 1.5px/1.4 Montserrat,sans-serif;margin-top:2px">Nemo enim ipsam voluptatem quia voluptas sit aspernatur aut odit aut fugit, sed quia consequuntur magni dolores eos qui ratione voluptatem.</div></div>
  <div class="foot"><span class="pg"></span><span class="flogo">Brim-Vane</span><span class="dots"><i></i><i></i><i></i></span><span class="web"><i></i>www.brim-vane.com</span></div>
</section>

<section class="slide" style="left:953px;top:465px">
  <div class="a" style="left:0;top:0;width:199px;height:50px;background:var(--green)"></div>
  <div class="ttl w" style="top:12px;color:#fff">Title Goes Here</div>
  <svg class="bg" viewBox="0 0 199 112">
    <g fill="var(--gold)" stroke="#fff" stroke-width=".8"><circle cx="38" cy="50" r="9"/><circle cx="95" cy="50" r="9"/><circle cx="157" cy="50" r="9"/></g>
    <g fill="none" stroke="#fff" stroke-width=".5"><circle cx="38" cy="50" r="4"/><circle cx="38" cy="50" r="2"/><path d="M92 53l6-6M94 47h4v4"/><rect x="154" y="47" width="6" height="6"/></g>
  </svg>
  <div class="a c" style="left:18px;top:62px;width:40px"><div class="h" style="font-size:2.4px;font-weight:600">Project Name</div><div class="p" style="font-size:1.6px;margin-top:1px">Lorem ipsum dolor sit amet, consectetur adipiscing elit, sed do eiusmod tempor incididunt ut labore et dolore magna aliqua. Ut enim ad minim veniam, quis nostrud</div></div>
  <div class="a c" style="left:75px;top:62px;width:40px"><div class="h" style="font-size:2.4px;font-weight:600">Project Name</div><div class="p" style="font-size:1.6px;margin-top:1px">Lorem ipsum dolor sit amet, consectetur adipiscing elit, sed do eiusmod tempor incididunt ut labore et dolore magna aliqua. Ut enim ad minim veniam, quis nostrud</div></div>
  <div class="a c" style="left:137px;top:62px;width:40px"><div class="h" style="font-size:2.4px;font-weight:600">Project Name</div><div class="p" style="font-size:1.6px;margin-top:1px">Lorem ipsum dolor sit amet, consectetur adipiscing elit, sed do eiusmod tempor incididunt ut labore et dolore magna aliqua. Ut enim ad minim veniam, quis nostrud</div></div>
  <div class="foot"><span class="pg"></span><span class="flogo">Brim-Vane</span><span class="dots"><i></i><i></i><i></i></span><span class="web"><i></i>www.brim-vane.com</span></div>
</section>

<!-- Row 5 -->
<section class="slide" style="left:725px;top:604px;background:#f6f6f6">
  <div class="ttl" style="top:9px">How It Works</div>
  <div class="a p c" style="left:12px;right:12px;top:18px;font-size:2.2px;color:#999">Sed ut perspiciatis unde omnis iste natus error sit voluptatem accusantium doloremque laudantium, totam rem aperiam, eaque ipsa quae ab illo inventore veritatis et quasi architecto beatae vitae dicta sunt explicabo. Nemo enim ipsam voluptatem quia voluptas sit aspernatur aut odit aut fugit.</div>
  <svg class="bg" viewBox="0 0 199 112">
    <g stroke="#fff" stroke-width="1.2"><line x1="38" y1="48" x2="38" y2="92"/><line x1="70" y1="48" x2="70" y2="92"/><line x1="103" y1="48" x2="103" y2="92"/><line x1="135" y1="48" x2="135" y2="92"/></g>
    <g fill="var(--gold)"><path d="M38 63a3.5 3.5 0 0 1 0 7z"/><path d="M70 63a3.5 3.5 0 0 1 0 7z"/><path d="M103 63a3.5 3.5 0 0 1 0 7z"/><path d="M135 63a3.5 3.5 0 0 1 0 7z"/><circle cx="172" cy="66.5" r="4.5"/></g>
    <path d="M170 66.5l1.5 1.5 2.5-3" fill="none" stroke="#222" stroke-width=".6"/>
    <g fill="none" stroke="#888" stroke-width=".35">
      <circle cx="22" cy="54" r="1.8"/><line x1="23.3" y1="55.3" x2="24.5" y2="56.5"/>
      <circle cx="54" cy="54" r="1.8"/><line x1="53.4" y1="56.5" x2="54.6" y2="56.5"/>
      <circle cx="87" cy="54.5" r="1.8" stroke-dasharray=".8 .5"/>
      <circle cx="119" cy="54.5" r="1.8"/><path d="M119 53.3v1.2l.8.6"/>
      <circle cx="152" cy="54.5" r="1.8"/><circle cx="152" cy="54.5" r=".7"/>
    </g>
    <g font-family="Montserrat,sans-serif" font-size="1.8" fill="#444" text-anchor="middle"><text x="22" y="61">RESEARCH</text><text x="54" y="61">IDEA</text><text x="87" y="61">PROCESS</text><text x="119" y="61">TIME</text><text x="152" y="61">GOAL</text></g>
  </svg>
  <div class="a p c" style="left:12px;top:63px;width:21px;font-size:1.3px">Lorem ipsum dolor sit amet, consectetur adipiscing elit, sed do eiusmod tempor incididunt ut labore.</div>
  <div class="a p c" style="left:44px;top:63px;width:21px;font-size:1.3px">Lorem ipsum dolor sit amet, consectetur adipiscing elit, sed do eiusmod tempor incididunt ut labore.</div>
  <div class="a p c" style="left:77px;top:63px;width:21px;font-size:1.3px">Lorem ipsum dolor sit amet, consectetur adipiscing elit, sed do eiusmod tempor incididunt ut labore.</div>
  <div class="a p c" style="left:109px;top:63px;width:21px;font-size:1.3px">Lorem ipsum dolor sit amet, consectetur adipiscing elit, sed do eiusmod tempor incididunt ut labore.</div>
  <div class="a p c" style="left:142px;top:63px;width:21px;font-size:1.3px">Lorem ipsum dolor sit amet, consectetur adipiscing elit, sed do eiusmod tempor incididunt ut labore.</div>
  <div class="foot"><span class="pg"></span><span class="flogo">Brim-Vane</span><span class="dots"><i></i><i></i><i></i></span><span class="web"><i></i>www.brim-vane.com</span></div>
</section>

<section class="slide" style="left:953px;top:604px">
  <div class="a" style="left:0;top:0;width:199px;height:50px;background:var(--gold)"></div>
  <div class="ttl" style="top:12px;color:#fff">Title Goes Here</div>
  <svg class="bg" viewBox="0 0 199 112">
    <g fill="var(--green)" stroke="#fff" stroke-width=".8"><circle cx="38" cy="50" r="9"/><circle cx="95" cy="50" r="9"/><circle cx="157" cy="50" r="9"/></g>
    <g fill="none" stroke="#fff" stroke-width=".5"><circle cx="38" cy="50" r="4"/><circle cx="38" cy="50" r="2"/><path d="M92 53l6-6M94 47h4v4"/><rect x="154" y="47" width="6" height="6"/></g>
  </svg>
  <div class="a c" style="left:18px;top:62px;width:40px"><div class="h" style="font-size:2.4px;font-weight:600">Project Name</div><div class="p" style="font-size:1.6px;margin-top:1px">Lorem ipsum dolor sit amet, consectetur adipiscing elit, sed do eiusmod tempor incididunt ut labore et dolore magna aliqua. Ut enim ad minim veniam, quis nostrud</div></div>
  <div class="a c" style="left:75px;top:62px;width:40px"><div class="h" style="font-size:2.4px;font-weight:600">Project Name</div><div class="p" style="font-size:1.6px;margin-top:1px">Lorem ipsum dolor sit amet, consectetur adipiscing elit, sed do eiusmod tempor incididunt ut labore et dolore magna aliqua. Ut enim ad minim veniam, quis nostrud</div></div>
  <div class="a c" style="left:137px;top:62px;width:40px"><div class="h" style="font-size:2.4px;font-weight:600">Project Name</div><div class="p" style="font-size:1.6px;margin-top:1px">Lorem ipsum dolor sit amet, consectetur adipiscing elit, sed do eiusmod tempor incididunt ut labore et dolore magna aliqua. Ut enim ad minim veniam, quis nostrud</div></div>
  <div class="foot"><span class="pg"></span><span class="flogo">Brim-Vane</span><span class="dots"><i></i><i></i><i></i></span><span class="web"><i></i>www.brim-vane.com</span></div>
</section>

</div>
</body>
</html>
```